Property development & Investment company Need a logo & business card design

Our name is KT Estates Australia Pty Ltd
Need logo & business card design

Target Market(s)

People dealing in commercial property

Industry/Entity Type

Business

Contact Information for Business Card

KT Estates Australia
Peter Dunmore Mobile0419 703 646
Email Peter@quillbarrow.com.au

Font styles to use
Sans Serif

Requirements
Must have
• company name
• contact details
Nice to have
• KT Estates Bold
• Australia Not Bold
Should not have
• To busy of a look

```html
<!DOCTYPE html>
<html lang="en">
<head>
<meta charset="utf-8">
<title>KT Estates Australia – Business Card</title>
<link href="https://fonts.googleapis.com/css2?family=Roboto:wght@400;500;700&display=swap" rel="stylesheet">
<style>
  :root {
    --backdrop: #1a1a1a;
    --card-white: #ffffff;
    --card-black: #1c1c1c;
    --ink-black: #050505;
    --gold: #d4ad2f;
    --text-dark: #111111;
    --text-light: #ffffff;
  }
  * { margin: 0; padding: 0; box-sizing: border-box; }
  html, body { width: 1200px; height: 800px; overflow: hidden; }
  body {
    background: var(--backdrop);
    font-family: "Roboto", Arial, sans-serif;
    position: relative;
  }
  .card {
    position: absolute;
    width: 520px;
    height: 300px;
    overflow: hidden;
    box-shadow: 0 14px 30px rgba(0,0,0,0.55);
  }
  .card--front { left: 50px; top: 250px; background: var(--card-white); }
  .card--back  { left: 630px; top: 250px; background: var(--card-black); }

  .card__shapes { position: absolute; inset: 0; }

  .wordmark {
    position: absolute;
    display: flex;
    align-items: center;
    gap: 12px;
    font-weight: 700;
    text-transform: uppercase;
    white-space: nowrap;
  }
  .wordmark__square { width: 14px; height: 14px; background: var(--gold); flex: none; }
  .wordmark__name { display: flex; flex-direction: column; line-height: 1.1; }
  .wordmark__main { font-size: 24px; letter-spacing: 1px; }
  .wordmark__sub { font-size: 13px; letter-spacing: 7.4px; margin-top: 4px; }

  .card--front .wordmark { left: 34px; top: 52px; color: var(--text-dark); }
  .card--back .wordmark { left: 50%; top: 50%; transform: translate(-50%, -50%); color: var(--text-light); }

  .contact {
    position: absolute;
    left: 34px;
    top: 170px;
    list-style: none;
    font-size: 14px;
    color: var(--text-dark);
  }
  .contact__item { display: flex; align-items: center; gap: 8px; margin-bottom: 6px; }
  .contact__icon {
    width: 16px; height: 16px; background: var(--gold);
    display: flex; align-items: center; justify-content: center; flex: none;
  }

  .person {
    position: absolute;
    right: 16px;
    top: 100px;
    text-align: right;
    white-space: nowrap;
  }
  .person__name { color: var(--text-light); font-weight: 700; font-size: 16px; letter-spacing: 0.5px; text-transform: uppercase; }
  .person__role { color: var(--gold); font-size: 11.5px; margin-top: 3px; }
</style>
</head>
<body>

  <section class="card card--front" aria-label="Business card front">
    <svg class="card__shapes" viewBox="0 0 520 300" aria-hidden="true">
      <polygon points="280,0 305,0 410,300 350,300" fill="var(--gold)"/>
      <polygon points="305,0 520,0 520,300 410,300" fill="var(--ink-black)"/>
    </svg>

    <div class="wordmark">
      <span class="wordmark__square"></span>
      <span class="wordmark__name">
        <span class="wordmark__main">KT Estates</span>
        <span class="wordmark__sub">Australia</span>
      </span>
    </div>

    <ul class="contact">
      <li class="contact__item">
        <span class="contact__icon">
          <svg width="10" height="10" viewBox="0 0 24 24"><path fill="#fff" d="M6.6 10.8a15.1 15.1 0 0 0 6.6 6.6l2.2-2.2c.3-.3.7-.4 1-.2 1.1.4 2.3.6 3.6.6.6 0 1 .4 1 1V20c0 .6-.4 1-1 1A17 17 0 0 1 3 4c0-.6.4-1 1-1h3.5c.6 0 1 .4 1 1 0 1.3.2 2.5.6 3.6.1.3 0 .7-.2 1z"/></svg>
        </span>
        <span>0438 512 907</span>
      </li>
      <li class="contact__item">
        <span class="contact__icon">
          <svg width="10" height="10" viewBox="0 0 24 24"><path fill="none" stroke="#fff" stroke-width="2.5" d="M3 6h18v12H3z M3 6l9 7 9-7"/></svg>
        </span>
        <span>peter@quillbarrow.com.au</span>
      </li>
    </ul>

    <div class="person">
      <p class="person__name">Peter Dunmore</p>
      <p class="person__role">Investment &amp; Development</p>
    </div>
  </section>

  <section class="card card--back" aria-label="Business card back">
    <div class="wordmark">
      <span class="wordmark__square"></span>
      <span class="wordmark__name">
        <span class="wordmark__main">KT Estates</span>
        <span class="wordmark__sub">Australia</span>
      </span>
    </div>
  </section>

</body>
</html>
```